Tallowmere Office Partners needs a new interactive and interesting website

We need an interesting, professional, modern and functional company website for Tallowmere Office Partners - a young IT Services company based out of Chennai, India.

Tallowmere Office Partners is a fully owned subsidiary of Hollin Cellarworks, one of the world's leading direct to consumer wine merchant.

We already have a registered company logo which must feature in the website.

We conceive, design, develop, test, implement and support IT solutions across the entire Hollin Cellarworks IT landscape. For ex : We currently run about 25 e-commerce websites for Hollin Cellarworks on KVM and Dot Net.

We would like to see our corporate colors used in the website. (Burgundy wine and wine green - source: www.tallowmereop.example)

We are looking at this website to communicate a fun, friendly and professionally managed company - reaching out to career seekers, prospective customers and general public.

For reference - The company name 'Tallowmere' is an inspiration from the Hollin Cellarworks lineage.

The second image with the world map is stickered on our main entrance to the office, I am not sure where this can be used -just putting it out there..
Updates

Please note that there are only a few more days to submit designs for this contest  !

I would appreciate if you can help posting your designs in time for our review and consideration.

Thanks.

Reason: Thanks for your inputs. We have a number of designers and a lot to digest and work with in the past few days. There has been a rush of new designs in the last few days Hence we will require more time to process these and make our decision. Hence i am requesting the contest to be open for more days. Regards, Suresh

Target Market(s)

Prospective job seekers who want to know more about the company and also wish to apply for a job vacancy
People wanting to know more about the company in general and our progress
People who want to see what we offer and how we can help them too - prospective customers
Companies that are interested in our IT Captive journey and are looking for a business opportunity

Industry/Entity Type

E-Commerce

Requirements
Must have
• Log In/ Register facility acting as a Single Sign on for Intranet (Employees)

Facility to post job vacancies (with an expiry date) and enable people to apply for a role and upload their CV/Resume.

Facility to Review Job applications

Facility for website visitors to contact Tallowmere Office Partners via an online 'Contact Us' form with a split of job seekers and business opportunities

Gallery facility to upload pictures regarding company events
Nice to have
• Less Cluttered and contemporary design
Some Wine/Vineyard inspirations will be good but not too much, the company is an IT services company

```html
<!DOCTYPE html>
<html lang="en">
<head>
<meta charset="utf-8">
<title>Tallowmere Office Partners</title>
<link rel="stylesheet" href="https://fonts.googleapis.com/css2?family=Open+Sans:wght@400;600;700&display=swap">
<style>
:root{
  --burgundy:#7e1045;
  --burgundy-dark:#5e0a33;
  --olive:#6e7a1f;
  --body-bg:#ecebe8;
  --ink:#333;
  --muted:#666;
  --heading-green:#3b4a1e;
  --footer:#333333;
  --footer-base:#282828;
  --white:#fff;
}
*{box-sizing:border-box;margin:0;padding:0}
html,body{width:806px;height:1200px;overflow:hidden;background:var(--white)}
body{font-family:"Open Sans",Arial,sans-serif;color:var(--ink)}
.page{position:relative;width:806px;height:1200px;overflow:hidden;background:var(--white)}
.abs{position:absolute}

/* header */
.brand{left:85px;top:8px;width:226px;height:63px;background:var(--burgundy);color:var(--white);padding:6px 0 0 16px}
.brand-mark{position:absolute;left:14px;top:14px;width:20px;height:20px;border-radius:50%;background:var(--white)}
.brand-name{position:absolute;left:42px;top:6px;font-size:23px;font-weight:700;line-height:1;letter-spacing:-.3px}
.brand-sub{position:absolute;left:42px;top:36px;font-size:14px;font-weight:400;line-height:1}
.phone{right:78px;top:26px;font-size:13px;color:var(--ink);display:flex;align-items:center;gap:6px}
.phone em{font-style:normal;color:var(--burgundy)}

.nav{left:78px;top:71px;width:650px;height:34px;background:var(--burgundy);display:flex;align-items:center;padding-left:15px}
.nav a{color:var(--white);text-decoration:none;font-size:10.5px;padding:2px 4px;margin-right:13px}
.nav a.current{background:var(--burgundy-dark)}
.search{position:absolute;right:15px;top:10px;width:171px;height:18px;background:var(--white);font-size:10px;color:var(--ink);padding:2px 9px;line-height:14px}
.search svg{position:absolute;right:4px;top:2px}

/* hero */
.hero{left:78px;top:110px;width:650px;height:277px;overflow:hidden}
.hero-photo{position:absolute;inset:0;background:linear-gradient(90deg,#f3f1ed 0%,#ece6dd 35%,#c9b7a0 58%,#8d6f56 78%,#6b4f3c 100%)}
.hero-curve{position:absolute;left:0;top:0}
.hero h1{position:absolute;left:17px;top:54px;font-size:20px;font-weight:400;color:var(--heading-green)}
.hero p{position:absolute;left:19px;top:92px;width:202px;font-size:9.6px;line-height:13.5px;color:#444}
.learn{position:absolute;left:19px;top:189px}
.learn span{position:absolute;left:10px;top:7px;font-size:12px;color:var(--ink)}

/* body */
.content-bg{left:78px;top:387px;width:650px;height:540px;background:var(--body-bg)}
.service{width:190px}
.service h3{font-size:13px;font-weight:400;line-height:14px;color:#222;padding-left:28px;min-height:28px}
.service svg{position:absolute;left:0;top:0}
.service p{font-size:7.4px;line-height:12.1px;color:#555}

.apply{left:520px;top:422px;width:223px;height:283px;background:linear-gradient(180deg,var(--burgundy) 60%,var(--burgundy-dark));color:var(--white);padding:7px 9px}
.apply h2{font-size:18px;font-weight:400;line-height:22px}
.apply label{position:absolute;left:9px;font-size:10.2px}
.field{position:absolute;left:9px;width:205px;height:19px;background:var(--white);border:1px solid #ccc;border-radius:1px}
.apply .area{height:47px}
.btn-olive{position:absolute;background:var(--olive);color:var(--white);font-size:11px;display:flex;align-items:center;justify-content:center;border-radius:1px}
.fold{left:728px;top:705px}

.gallery-title{left:98px;top:716px;font-size:13px;color:#222}
.rule{left:98px;top:741px;width:609px;height:1px;background:#cfcfcc}
.thumb{top:755px;width:148px;height:99px;border:2px solid var(--white);box-shadow:0 1px 3px rgba(0,0,0,.25)}
.upload{z-index:5;left:343px;top:876px;width:125px;height:30px;font-size:12px}

/* footer */
.footer{left:78px;top:885px;width:650px;height:302px;background:var(--footer);color:#ddd}
.footer-curve{left:78px;top:884px}
.footer-base{left:78px;top:1157px;width:650px;height:30px;background:var(--footer-base);color:#ddd;font-size:8px;text-align:center;line-height:30px}
.f-brand{left:93px;top:944px;color:var(--white)}
.f-brand .brand-mark{left:0;top:6px;width:14px;height:14px}
.f-brand .n{position:absolute;left:20px;top:0;font-size:17px;font-weight:700;line-height:1;white-space:nowrap}
.f-brand .s{position:absolute;left:20px;top:20px;font-size:10.5px;white-space:nowrap}
.f-about{left:93px;top:986px;width:200px;font-size:10.3px;line-height:14.8px;color:#e6e6e6}
.f-address{left:114px;top:1058px;font-size:8.3px;line-height:12.1px;color:#e6e6e6}
.f-pin{left:94px;top:1103px}
.f-title{font-size:13.5px;color:#f0f0f0}
.f-nav{left:349px;top:992px;list-style:none}
.f-nav li{font-size:10.3px;line-height:14.9px;color:#cfcfcf}
.f-nav li.current{color:var(--burgundy)}
.f-field{position:absolute;left:507px;width:205px;background:var(--white);border:1px solid #bbb;font-size:8px;color:#555;padding:3px 7px}
.send{left:507px;top:1117px;width:85px;height:22px;background:var(--burgundy);color:var(--white);font-size:12px;display:flex;align-items:center;justify-content:center;box-shadow:0 2px 3px rgba(0,0,0,.4)}
</style>
</head>
<body>
<div class="page">

  <header>
    <div class="brand abs">
      <span class="brand-mark"></span>
      <span class="brand-name">Tallowmere</span>
      <span class="brand-sub">Office Partners</span>
    </div>
    <div class="phone abs">
      <svg width="20" height="20" viewBox="0 0 24 24" aria-hidden="true"><path fill="#7e1045" d="M6.6 10.8a15 15 0 0 0 6.6 6.6l2.2-2.2c.3-.3.7-.4 1-.2 1.1.4 2.3.6 3.6.6.6 0 1 .4 1 1V20c0 .6-.4 1-1 1A17 17 0 0 1 3 4c0-.6.4-1 1-1h3.5c.6 0 1 .4 1 1 0 1.3.2 2.5.6 3.6.1.3 0 .7-.2 1z"/></svg>
      <span><em>Tel:</em> +91 (44) 5550 0100</span>
    </div>
    <nav class="nav abs">
      <a class="current" href="#">Home</a>
      <a href="#">About us</a>
      <a href="#">Clients</a>
      <a href="#">Services</a>
      <a href="#">Careers</a>
      <a href="#">Contact us</a>
      <div class="search">Search
        <svg width="14" height="14" viewBox="0 0 14 14" aria-hidden="true"><circle cx="6" cy="6" r="4.6" fill="none" stroke="#222" stroke-width="1.6"/><line x1="9.4" y1="9.4" x2="13" y2="13" stroke="#222" stroke-width="1.8"/></svg>
      </div>
    </nav>
  </header>

  <section class="hero abs">
    <div class="hero-photo" role="img" aria-label="Smiling man at a laptop holding a glass of red wine in a bright café"></div>
    <svg class="hero-curve" width="650" height="277" viewBox="0 0 650 277" aria-hidden="true">
      <path d="M0,245 Q325,305 650,245 L650,277 L0,277 Z" fill="#ecebe8"/>
    </svg>
    <h1>Delivering IT Excellence</h1>
    <p>Welcome to Tallowmere Office Partners, an emerging provider of global IT consulting and software services. We are part of the Hollin Cellarworks group, a family run business and the world's largest multi-channel home delivery wine merchant.</p>
    <div class="learn">
      <svg width="115" height="27" viewBox="0 0 115 27" aria-hidden="true"><path d="M0,0 H102 L115,13.5 L102,27 H0 Z" fill="#fff"/></svg>
      <span>LEARN MORE</span>
    </div>
  </section>

  <div class="content-bg abs"></div>

  <section>
    <div class="service abs" style="left:98px;top:424px">
      <svg width="22" height="20" viewBox="0 0 22 20" aria-hidden="true"><rect x="1" y="1" width="20" height="14" rx="1" fill="none" stroke="#7e1045" stroke-width="2"/><rect x="5" y="5" width="12" height="2" fill="#7e1045"/><rect x="5" y="9" width="8" height="2" fill="#7e1045"/><rect x="8" y="16" width="6" height="3" fill="#7e1045"/></svg>
      <h3>Packaged Applications</h3>
      <p>Lorem ipsum dolor sit amet, consectetur adipisicing elit, sed do eiusmod tempor incididunt ut labore et dolore magna aliqua. Ut enim ad minim veniam, quis nostrud exercitation ullamco laboris nisi ut aliquip ex ea commodo consequat.</p>
    </div>
    <div class="service abs" style="left:309px;top:424px">
      <svg width="22" height="22" viewBox="0 0 22 22" aria-hidden="true"><circle cx="11" cy="11" r="10" fill="none" stroke="#7e1045" stroke-width="2"/><ellipse cx="11" cy="11" rx="4" ry="10" fill="none" stroke="#7e1045" stroke-width="1.5"/><line x1="1" y1="11" x2="21" y2="11" stroke="#7e1045" stroke-width="1.5"/><line x1="3" y1="6" x2="19" y2="6" stroke="#7e1045" stroke-width="1.2"/><line x1="3" y1="16" x2="19" y2="16" stroke="#7e1045" stroke-width="1.2"/></svg>
      <h3>Enterprise Application Integration</h3>
      <p>Lorem ipsum dolor sit amet, consectetur adipisicing elit, sed do eiusmod tempor incididunt ut labore et dolore magna aliqua. Ut enim ad minim veniam, quis nostrud exercitation ullamco laboris nisi ut aliquip ex ea commodo consequat.</p>
    </div>
    <div class="service abs" style="left:98px;top:565px">
      <svg width="22" height="22" viewBox="0 0 22 22" aria-hidden="true"><g fill="#7e1045"><circle cx="11" cy="11" r="7"/><rect x="9" y="0" width="4" height="22"/><rect x="0" y="9" width="22" height="4"/><rect x="9" y="0" width="4" height="22" transform="rotate(45 11 11)"/><rect x="9" y="0" width="4" height="22" transform="rotate(-45 11 11)"/></g><circle cx="11" cy="11" r="3" fill="#ecebe8"/></svg>
      <h3>Application Development &amp; Maintenance</h3>
      <p>Lorem ipsum dolor sit amet, consectetur adipisicing elit, sed do eiusmod tempor incididunt ut labore et dolore magna aliqua. Ut enim ad minim veniam, quis nostrud exercitation ullamco laboris nisi ut aliquip ex ea commodo consequat.</p>
    </div>
    <div class="service abs" style="left:309px;top:565px">
      <svg width="24" height="20" viewBox="0 0 24 20" aria-hidden="true"><path d="M1,3 Q6,1 11,4 V19 Q6,16 1,18 Z M13,4 Q18,1 23,3 V18 Q18,16 13,19 Z" fill="#7e1045"/></svg>
      <h3 style="padding-top:2px">Digital Commerce</h3>
      <p>Lorem ipsum dolor sit amet, consectetur adipisicing elit, sed do eiusmod tempor incididunt ut labore et dolore magna aliqua. Ut enim ad minim veniam, quis nostrud exercitation ullamco laboris nisi ut aliquip ex ea commodo consequat.</p>
    </div>
  </section>

  <aside class="apply abs">
    <h2>Apply For A Job</h2>
    <label style="top:38px">Your Name *</label>
    <div class="field" style="top:56px"></div>
    <label style="top:86px">Your Phone Number *</label>
    <div class="field" style="top:104px"></div>
    <label style="top:135px">Your Address *</label>
    <div class="field" style="top:153px"></div>
    <label style="top:180px">Your Comment *</label>
    <div class="field area" style="top:198px"></div>
    <div class="btn-olive" style="left:9px;top:253px;width:99px;height:24px">Register Now</div>
  </aside>
  <svg class="fold abs" width="15" height="12" viewBox="0 0 15 12" aria-hidden="true"><path d="M0,0 H15 L0,12 Z" fill="#4a0828"/></svg>

  <section>
    <h2 class="gallery-title abs" style="font-weight:400">Our Gallery</h2>
    <div class="rule abs"></div>
    <div class="thumb abs" style="left:98px;background:linear-gradient(135deg,#e9ecef,#b9a58f 55%,#7c8fb4)" role="img" aria-label="Student smiling at a computer workstation"></div>
    <div class="thumb abs" style="left:252px;background:linear-gradient(135deg,#8a7c72,#c35a4d 50%,#5a5d66)" role="img" aria-label="Group of students working together at computers"></div>
    <div class="thumb abs" style="left:405px;background:linear-gradient(135deg,#c9a88f,#8f7a52 45%,#c8452e)" role="img" aria-label="Young people gathered around a desk in a classroom"></div>
    <div class="thumb abs" style="left:559px;background:linear-gradient(135deg,#dfe3e6,#b98f73 55%,#5d7aa0)" role="img" aria-label="Instructor pointing at a monitor for a group of students"></div>
  </section>

  <footer>
    <div class="footer abs"></div>
    <svg class="footer-curve abs" width="650" height="46" viewBox="0 0 650 46" aria-hidden="true">
      <path d="M0,0 L0,1 Q325,85 650,1 L650,0 Z" fill="#ecebe8"/>
      <path d="M0,1 Q325,85 650,1" fill="none" stroke="#8a8a8a" stroke-width="1.5"/>
    </svg>

    <div class="f-brand abs">
      <span class="brand-mark"></span>
      <span class="n">Tallowmere</span>
      <span class="s">Office Partners</span>
    </div>
    <p class="f-about abs">Lorem ipsum dolor sit amet, consectetur adipisicing elit, sed do eiusmod tempor incididunt ut labore et dolore magna aliqua.</p>
    <svg class="f-pin abs" width="13" height="17" viewBox="0 0 13 17" aria-hidden="true"><path d="M6.5,0 A6.5,6.5 0 0 1 13,6.5 C13,11 6.5,17 6.5,17 C6.5,17 0,11 0,6.5 A6.5,6.5 0 0 1 6.5,0 Z" fill="#fff"/><circle cx="6.5" cy="6.5" r="2.6" fill="#333"/></svg>
    <address class="f-address abs" style="font-style:normal">
      Tallowmere Office Partners Pvt. Ltd.<br>
      4th Floor, Larkspur Point<br>
      Unit C12 Marigold Industrial Estate<br>
      Velachery<br>
      Chennai, 600042<br>
      Tamil Nadu
    </address>

    <h3 class="f-title abs" style="left:347px;top:958px;font-weight:400">Navigation</h3>
    <ul class="f-nav abs">
      <li class="current">Home</li>
      <li>About us</li>
      <li>Clients</li>
      <li>Services</li>
      <li>Careers</li>
      <li>Contact us</li>
    </ul>

    <h3 class="f-title abs" style="left:506px;top:961px;font-weight:400">Contact Us</h3>
    <div class="f-field" style="top:999px;height:20px">Your Name (required)</div>
    <div class="f-field" style="top:1029px;height:20px">Subject</div>
    <div class="f-field" style="top:1059px;height:47px">Your Message</div>
    <div class="send abs">Send</div>

    <div class="footer-base abs">Copyright 2014 © Tallowmere All rights reserved.</div>
  </footer>

  <div class="btn-olive upload abs">Upload Picture</div>

</div>
</body>
</html>
```